Restaurant needs promotional material

We need a design for a "free welcome cocktail on your next visit" flyer. The flyer must have a black background and be contemporary. Our logo is the name of the restaurant which is "Ember Nook" in edwardian script font with italic selected.

There must be a section for terms and conditions, which are:
1 free cocktail for every main course ordered from our evening menu over the value of 9.95€ (not including taxes). The number of free cocktails cannot exceed the number of main courses ordered from your previous visit. This offer is only valid when you present both this flyer and your receipt from your previous visit. This offer does not include ice cream cocktails. This offer cannot be used in conjunction with any other offer or promotion. Limit 1 free cocktail per person. We reserve the right to final interpretation of this offer and can cancel the offer at any time.

A space must also be left where we can write a "valid until" date.

The uploaded photos are a picture of our cocktail menu and the publicity we are currently running, so you can get a feel for your design.

Thanks

Industry/Entity Type

Restaurant

Colors
000000

Requirements
Must have
• Also included in the flyer is the text " Please present this flyer along with your bill from your previous visit upon arrival.
• Pictures of cocktails!

```html
<!DOCTYPE html>
<html lang="en">
<head>
<meta charset="utf-8">
<title>Ember Nook – Free Welcome Cocktail Flyer</title>
<link rel="stylesheet" href="https://fonts.googleapis.com/css2?family=Marcellus&family=Questrial&family=Didact+Gothic&display=swap">
<style>
  :root {
    --flyer-black: #050506;
    --accent-pink: #e8287f;
    --text-white: #f2f2f2;
    --text-soft: #d9d9d9;
    --smoke-grey: #6f6f74;
    --drink-red: #c8343f;
    --drink-green: #6f9a2a;
    --drink-amber: #e08a1c;
    --page-bg: #1a1a1a;
  }
  * { margin: 0; padding: 0; box-sizing: border-box; }
  html, body {
    width: 1200px; height: 664px; overflow: hidden;
    background: var(--page-bg);
  }
  .flyer {
    position: relative;
    width: 1200px; height: 664px;
    background: var(--flyer-black);
    overflow: hidden;
    font-family: "Didact Gothic", sans-serif;
    color: var(--text-white);
  }
  .cocktail-photo {
    position: absolute;
    left: 470px; top: 0;
    width: 730px; height: 664px;
    background:
      radial-gradient(ellipse 120px 170px at 200px 400px, rgba(220,220,215,0.35), transparent 70%),
      radial-gradient(ellipse 130px 160px at 360px 320px, rgba(200,52,63,0.75), transparent 72%),
      radial-gradient(ellipse 130px 160px at 510px 350px, rgba(111,154,42,0.7), transparent 72%),
      radial-gradient(ellipse 140px 170px at 660px 330px, rgba(224,138,28,0.8), transparent 72%),
      radial-gradient(ellipse 320px 220px at 330px 130px, rgba(111,111,116,0.45), transparent 75%),
      radial-gradient(ellipse 300px 200px at 520px 560px, rgba(111,111,116,0.3), transparent 75%),
      linear-gradient(90deg, var(--flyer-black) 0%, rgba(5,5,6,0) 22%);
  }
  .offer-title {
    position: absolute;
    left: 37px; top: 28px;
    font-family: "Marcellus", serif;
    font-weight: 400;
    font-size: 60px;
    line-height: 67px;
    letter-spacing: 2px;
    color: var(--accent-pink);
    text-transform: uppercase;
  }
  .offer-subtitle {
    position: absolute;
    left: 44px; top: 226px;
    font-family: "Questrial", sans-serif;
    font-size: 35px;
    color: var(--text-soft);
    letter-spacing: 0.5px;
  }
  .conditions {
    position: absolute;
    left: 37px; top: 322px;
    width: 436px;
  }
  .conditions-heading {
    font-size: 13px;
    font-weight: 400;
    letter-spacing: 0.5px;
    text-transform: uppercase;
    margin-bottom: 9px;
  }
  .conditions-text {
    font-size: 12.6px;
    line-height: 20.5px;
    text-align: justify;
  }
  .arrival-note {
    position: absolute;
    left: 35px; top: 560px;
    width: 440px;
    font-size: 15px;
    line-height: 19px;
    color: var(--accent-pink);
  }
  .valid-until {
    position: absolute;
    left: 37px; top: 621px;
    width: 820px; height: 20px;
    padding-left: 6px;
    background: linear-gradient(90deg, #ffffff 0%, #ffffff 8%, #9a9a9a 40%, rgba(80,80,80,0.6) 80%, rgba(5,5,6,0) 100%);
    color: #111;
    font-size: 12.5px;
    line-height: 20px;
  }
  .brand-name {
    position: absolute;
    right: 42px; top: 582px;
    font-family: "Marcellus", serif;
    font-size: 48px;
    line-height: 1;
    color: var(--text-white);
  }
</style>
</head>
<body>
  <main class="flyer">
    <div class="cocktail-photo" role="img" aria-label="Photograph of four martini cocktails in a row – clear with olive and lemon twist, red with blackberry, green, and amber with cherry – wrapped in drifting smoke"></div>

    <h1 class="offer-title">Free<br>Welcome<br>Cocktail</h1>
    <p class="offer-subtitle">on your next visit</p>

    <section class="conditions">
      <h2 class="conditions-heading">Conditions</h2>
      <p class="conditions-text">1 free cocktail for every main course ordered from our evening menu over the value of 9.95€ (not including taxes). The number of free cocktails cannot exceed the number of main courses ordered from your previous visit. This offer is only valid when you present both this flyer and your receipt from your previous visit. This offer does not include ice cream cocktails. This offer cannot be used in conjunction with any other offer or promotion. Limit 1 free cocktail per person. We reserve the right to final interpretation of this offer and can cancel the offer at any time.</p>
    </section>

    <p class="arrival-note">Please present this flyer along with your bill from your previous visit upon arrival.</p>

    <div class="valid-until">valid until:</div>

    <p class="brand-name">Ember Nook</p>
  </main>
</body>
</html>
```